Postcard Design Project

landscape company. We do yard maintenance, tree service, hardscapes, stone, custom limestone, bobcat and dumptruck work, I would like our phone numbers: 205.555.0147 and 205.555.0182 on there as well as email: dorvelyards@mailnestr.com. We offer free estimates. look at our chatterloop page and include chatterloop logo on postcard

```html
<!DOCTYPE html>
<html lang="en">
<head>
<meta charset="utf-8">
<title>Dorvel Yards Postcard</title>
<link rel="stylesheet" href="https://fonts.googleapis.com/css2?family=Archivo:wght@400;700;800&family=Josefin+Sans:wght@400;600&display=swap">
<style>
:root{
  --stage:#d9d9d9;
  --card:#ffffff;
  --green:#157a3c;
  --green-dark:#0f5e2d;
  --lime:#c8e021;
  --leaf:#7cc242;
  --ink:#111111;
  --band:#000000;
}
*{box-sizing:border-box;margin:0;padding:0}
html,body{width:891px;height:1200px;overflow:hidden;background:var(--stage)}
.card{position:absolute;left:30px;width:831px;height:554px;background:var(--card);border-radius:10px;overflow:hidden;box-shadow:0 4px 14px rgba(0,0,0,.18)}
.front{top:30px}
.back{top:616px}
.shapes{position:absolute;inset:0}
.brand{position:absolute;font-family:"Josefin Sans",sans-serif;font-weight:600;color:var(--green);line-height:.95;text-align:center}
.front .brand{left:40px;top:70px;width:250px;font-size:44px}
.brand-mark{display:block;width:44px;height:44px;border-radius:50%;background:var(--green);margin:0 auto 14px}
.headline{position:absolute;left:150px;top:218px;width:660px;font-family:"Archivo",sans-serif;font-weight:800;font-size:34px;color:var(--lime);letter-spacing:-.5px;white-space:nowrap}
.services{position:absolute;left:38px;top:296px;list-style:none;font-family:"Archivo",sans-serif;font-weight:700;font-size:15px;color:#fff;line-height:21px}
.services li::before{content:"•";margin-right:7px}
.social{position:absolute;left:38px;top:460px;display:flex;align-items:center;gap:7px;font-family:"Archivo",sans-serif;font-weight:700;font-size:14px;color:#fff}
.social i{width:14px;height:14px;background:#fff;display:block}
.contact{position:absolute;font-family:"Archivo",sans-serif;font-weight:700;color:var(--ink);white-space:nowrap}
.front .phones{left:340px;top:428px;font-size:30px}
.front .email{left:370px;top:468px;font-size:23px}
.back-panel{position:absolute;left:0;top:0;width:415px;height:554px;background:var(--green)}
.back-logo{position:absolute;left:120px;top:26px;width:175px;height:92px;background:#fff;display:flex;align-items:center;justify-content:center}
.back .brand{font-size:24px;width:175px}
.back .brand-mark{width:24px;height:24px;margin-bottom:6px}
.back-title{position:absolute;left:30px;top:136px;width:355px;text-align:center;font-family:"Josefin Sans",sans-serif;font-size:22px;color:#fff;line-height:1.15}
.back-title b{font-weight:600}
.lorem{position:absolute;left:36px;top:232px;width:343px;text-align:center;font-family:"Josefin Sans",sans-serif;font-size:13.5px;color:#fff;line-height:1.35}
.back-photos{position:absolute;left:0;top:372px;width:415px;height:80px;display:flex;gap:4px}
.back-photos div{flex:1}
.back .phones{left:30px;top:468px;font-size:22px;color:#fff}
.back .email{left:30px;top:500px;font-size:20px;color:#fff}
</style>
</head>
<body>

<section class="card front">
  <svg class="shapes" width="831" height="554" viewBox="0 0 831 554">
    <defs>
      <linearGradient id="house" x1="0" y1="0" x2="0" y2="1">
        <stop offset="0" stop-color="#d9a25a"/><stop offset=".45" stop-color="#e6e3da"/><stop offset="1" stop-color="#8a9a63"/>
      </linearGradient>
      <linearGradient id="grass" x1="0" y1="0" x2="0" y2="1">
        <stop offset="0" stop-color="#ffffff"/><stop offset=".45" stop-color="#eef6e2"/><stop offset="1" stop-color="#4fa82c"/>
      </linearGradient>
    </defs>
    <polygon points="360,0 831,0 831,212 300,212" fill="url(#house)" role="img" aria-label="Photo of a large white colonial home with autumn trees"/>
    <rect x="0" y="404" width="831" height="150" fill="url(#grass)" role="img" aria-label="Green grass blades along the bottom edge"/>
    <rect x="0" y="212" width="831" height="56" fill="var(--band)"/>
    <polygon points="0,268 245,268 175,554 0,554" fill="var(--green)"/>
    <polygon points="245,268 395,268 350,412 210,412" fill="#9aa59a" role="img" aria-label="Photo of a stone fountain at a front entrance"/>
    <polygon points="399,268 560,268 512,412 354,412" fill="#8a4f2c" role="img" aria-label="Photo of a stone fireplace with holiday stockings"/>
    <polygon points="564,268 831,268 831,412 516,412" fill="#9a7a5c" role="img" aria-label="Photo of a stone turret on a house exterior"/>
  </svg>
  <div class="brand"><span class="brand-mark"></span>DORVEL<br>YARDS</div>
  <div class="headline">A Beautiful yard is a Happy Place</div>
  <ul class="services">
    <li>Yard Maintenance</li><li>Tree Service</li><li>Hardscapes</li><li>Stone</li><li>Custom Limestone</li><li>Bobcat</li><li>Dumptruck Work</li>
  </ul>
  <div class="social"><i></i>chatterloop</div>
  <div class="contact phones">205.555.0147 | 205.555.0182</div>
  <div class="contact email">dorvelyards@mailnestr.com</div>
</section>

<section class="card back">
  <div class="back-panel"></div>
  <div class="back-logo"><div class="brand"><span class="brand-mark"></span>DORVEL YARDS</div></div>
  <div class="back-title">We Provide <b>Professional<br>Lawn Care &amp;</b><br>Graening Services</div>
  <p class="lorem">Lorem Ipsum is simply dummy text of the printing and typesetting industry. Lorem Ipsum has been the industry's standard dummy text ever since the 1500s, when an unknown printer took a galley of type and scrambled it to make a type specimen book.</p>
  <div class="back-photos">
    <div style="background:#7a4a2a" role="img" aria-label="Photo of a decorated fireplace mantel"></div>
    <div style="background:#6e6557" role="img" aria-label="Photo of a stone paved patio"></div>
    <div style="background:#b9ad96" role="img" aria-label="Photo of a stone archway entrance"></div>
  </div>
  <div class="contact phones">205.555.0147 | 205.555.0182</div>
  <div class="contact email">dorvelyards@mailnestr.com</div>
</section>

</body>
</html>
```